Nordisk Husforum

Company is in: Denmark - Copenhagen
It sells: Restaurants and café buildings
Companys age: 25 years
Main benefit: trust with over 25 years experience

```html
<!DOCTYPE html>
<html lang="en">
<head>
<meta charset="utf-8">
<title>Nordisk Husforum</title>
<link rel="stylesheet" href="https://fonts.googleapis.com/css2?family=Arimo:ital,wght@0,400;0,700;1,400&family=Crimson+Text:wght@700&display=swap">
<style>
  :root {
    --ink: #1e1e1e;
    --text: #222;
    --blue: #3a5fcd;
    --link: #2f5bc6;
    --red: #c41e1e;
    --tab-red: #d63a3a;
    --nav-top: #4a4a4a;
    --nav-bottom: #111;
    --band-top: #f3f3f3;
    --band-bottom: #e5e6e7;
    --rule: #d6d6d6;
  }
  * { box-sizing: border-box; margin: 0; padding: 0; }
  html, body { width: 1200px; height: 1198px; overflow: hidden; background: #fff; }
  body { position: relative; font-family: "Arimo", Arial, sans-serif; color: var(--text); }

  .brand { position: absolute; left: 160px; top: 36px; font-family: "Crimson Text", Georgia, serif; font-weight: 700; font-size: 29px; letter-spacing: 0.3px; color: var(--ink); }

  .search { position: absolute; left: 830px; top: 35px; width: 230px; height: 31px; border: 1px solid #bcbcbc; border-radius: 6px; background: #fff; box-shadow: inset 0 1px 2px rgba(0,0,0,.08); }
  .search span { position: absolute; left: 14px; top: 8px; font-size: 12px; font-style: italic; color: #555; }
  .search svg { position: absolute; right: 14px; top: 6px; }

  .nav { position: absolute; left: 160px; top: 102px; width: 900px; height: 51px; border-radius: 7px; background: linear-gradient(var(--nav-top), #262626 50%, var(--nav-bottom)); border: 1px solid #000; display: flex; align-items: center; justify-content: space-between; padding: 0 21px; }
  .nav a { color: #fff; text-decoration: none; font-size: 18px; }

  .hero { position: absolute; left: 160px; top: 180px; width: 900px; height: 450px; border-radius: 9px; overflow: hidden;
    background: linear-gradient(100deg, #e4ded6 0%, #d2bfae 30%, #c3a68c 48%, #8a6a4c 60%, #d9cbb8 78%, #e9e2d6 100%); }
  .hero-caption { position: absolute; left: 600px; top: 25px; width: 280px; color: #fff; font-weight: 700; font-size: 24px; line-height: 25px; }
  .dots { position: absolute; left: 750px; top: 420px; display: flex; gap: 6px; }
  .dots i { width: 14px; height: 14px; border-radius: 50%; background: #eee; display: block; }
  .dots i.on { background: #c9403f; }

  .question-tab { position: absolute; left: 1165px; top: 180px; width: 40px; height: 180px; border-radius: 8px 0 0 8px; background: linear-gradient(90deg, #c72d2d, var(--tab-red)); border: 1px solid #a82222; }
  .question-tab span { position: absolute; left: 50%; top: 50%; transform: translate(-50%,-50%) rotate(-90deg); white-space: nowrap; color: #fff; font-style: italic; font-size: 16px; }

  .welcome { position: absolute; left: 160px; top: 649px; width: 890px; }
  .welcome h1 { font-size: 25px; color: var(--blue); font-weight: 700; margin-bottom: 6px; }
  .welcome p { font-size: 16px; line-height: 25px; }

  .band { position: absolute; left: 0; top: 829px; width: 1200px; height: 331px; background: linear-gradient(var(--band-top), var(--band-bottom)); border-top: 2px solid #e0e0e0; }
  .venue { position: absolute; top: 22px; width: 260px; }
  .venue h2 { font-size: 25px; color: var(--red); font-weight: 700; margin-left: 5px; margin-bottom: 8px; }
  .venue .photo { width: 255px; height: 130px; border: 5px solid #fff; box-shadow: 0 3px 4px rgba(0,0,0,.12); }
  .venue p { font-size: 14px; line-height: 21px; margin-top: 9px; color: #111; }
  .venue a { display: inline-block; margin-top: 3px; font-size: 14px; font-style: italic; color: var(--link); }
  .divider { position: absolute; top: 60px; width: 1px; height: 225px; background: var(--rule); }

  .footer { position: absolute; right: 140px; top: 1174px; font-size: 12px; color: #111; }
</style>
</head>
<body>
  <div class="brand">NORDISK HUSFORUM</div>

  <div class="search">
    <span>Search...</span>
    <svg width="20" height="20" viewBox="0 0 20 20"><circle cx="12" cy="8" r="5.5" fill="none" stroke="#222" stroke-width="2"/><line x1="8" y1="12" x2="2" y2="18" stroke="#222" stroke-width="3" stroke-linecap="round"/></svg>
  </div>

  <nav class="nav">
    <a href="#">Home</a><a href="#">For Sale</a><a href="#">Links/Download</a><a href="#">Newsletter</a><a href="#">About Us</a><a href="#">Contact Us</a>
  </nav>

  <section class="hero" role="img" aria-label="Banquet table set with folded napkins, glasses and a fruit bowl">
    <p class="hero-caption">Lorem ipsum dolor sit amet, consectetuer adipiscing elit. Aenean commodo ligula eget dolor.</p>
    <div class="dots"><i class="on"></i><i></i><i></i><i></i><i></i><i></i></div>
  </section>

  <div class="question-tab"><span>Have a question?</span></div>

  <section class="welcome">
    <h1>Welcome to NORDISK HUSFORUM</h1>
    <p>Lorem ipsum dolor sit amet, consectetuer adipiscing elit. Aenean commodo ligula eget dolor. Aenean massa. Cum sociis natoque penatibus et magnis dis parturient montes, nascetur ridiculus mus. Donec quam felis, ultricies nec, pellentesque eu, pretium quis, sem. Nulla consequat massa quis enim. Donec pede justo, fringilla vel, aliquet nec, vulputate eget, arcu. In enim justo, rhoncus ut, imperdiet a, venenatis vitae, justo. Nullam dictum felis eu pede mollis pretium. Integer tincidunt. Cras dapibus. Vivamus elementum semper nisi.</p>
  </section>

  <section class="band">
    <article class="venue" style="left:160px">
      <h2>Restaurant</h2>
      <div class="photo" role="img" aria-label="Restaurant dining room with purple lit trees" style="background:linear-gradient(#7a5aa8,#a58cc8 45%,#5a4a3a)"></div>
      <p>Lorem ipsum dolor sit amet, con-<br>sectetuer adipiscing elit. Aenean com-<br>modo ligula eget dolor.</p>
      <a href="#">Read more...</a>
    </article>
    <div class="divider" style="left:448px"></div>
    <article class="venue" style="left:480px">
      <h2>Cafe</h2>
      <div class="photo" role="img" aria-label="Cafe table with wine glasses and flowers" style="background:linear-gradient(#c99a2e,#e2be5a 55%,#8a3a1e)"></div>
      <p>Lorem ipsum dolor sit amet, con-<br>sectetuer adipiscing elit. Aenean com-<br>modo ligula eget dolor.</p>
      <a href="#">Read more...</a>
    </article>
    <div class="divider" style="left:767px"></div>
    <article class="venue" style="left:800px">
      <h2>Pab</h2>
      <div class="photo" role="img" aria-label="Brick corner pub building with dark shopfront" style="background:linear-gradient(#7a6a5e,#5a4a40 60%,#1e1a1a)"></div>
      <p>Lorem ipsum dolor sit amet, con-<br>sectetuer adipiscing elit. Aenean com-<br>modo ligula eget dolor.</p>
      <a href="#">Read more...</a>
    </article>
  </section>

  <footer class="footer">Copyright © 2011 NORDISK HUSFORUM All rights reserved</footer>
</body>
</html>
```